Business card design needed

the business is HR Consulting, but its for SME businesses who cant afford a permanent HR person. We sell an HR info system to help them meet minimum employment legislation but with this hope they then require us on a monthly subscription to phone or email us for HR advice. We are HR qualified mums working from home

So we will be partners to HR and Payroll systems known as unify HR and Tally

Target Market(s)

Small to medium businesses so not black and overly corporate, but having said that many are accounting businesses

Industry/Entity Type

Business

Contact Information for Business Card

Name of the company: Maple HR

Me:Marta Oldenbrook
Title:Managing Director

m: 0438 615 209
e: marta@maplehr.com.au
w: www.maplehr.com.au

What we do: HR Consulting, HR Systems and support, Payroll Advice

Requirements
Nice to have
• there is a company already out there known as Harbor professionals. I like the leaves at the end as I wanted something different like this to the usual business logos but still professional. I wanted a symbol to show calm, positive, ease flow going up ,etc. but realise they have the leaves and possibly cant copy, or can we?..( kite??, something calm and positive)dont know!!. Green and blue needed to be in it as nature and calm as well. I love the colours of www.staffingfundco.com ( attached the colours), as well as the calm wave line underneath. have a look as while they use green and blue I loved the purple colour thrown in there.Green and blue on their own are so overused. I want vibrant. I want double sided and when on a table I want it to stand out so maybe the purple colour (as per the colours on the fund website) solid on one side with just the 3 services we provide and personal and company name on front but need some creativity from you guys.

```html
<!DOCTYPE html>
<html lang="en">
<head>
<meta charset="utf-8">
<title>Maple HR – Business Card</title>
<link rel="stylesheet" href="https://fonts.googleapis.com/css2?family=Source+Sans+3:ital,wght@0,400;0,600;1,700&display=swap">
<style>
  :root {
    --card-bg: #c6d2d2;
    --brand-ink: #3c3e3f;
    --text-ink: #2e4442;
    --accent-purple: #9a5ef2;
  }
  html, body {
    margin: 0;
    padding: 0;
    overflow: hidden;
    background: var(--card-bg);
  }
  .card {
    position: relative;
    width: 1200px;
    height: 693px;
    background: var(--card-bg);
    font-family: "Source Sans 3", "Myriad Pro", Arial, sans-serif;
    color: var(--text-ink);
    overflow: hidden;
  }
  .brand-name {
    position: absolute;
    left: 105px;
    top: 135px;
    margin: 0;
    font-size: 105px;
    font-weight: 600;
    line-height: 1;
    letter-spacing: -1px;
    color: var(--brand-ink);
  }
  .divider {
    position: absolute;
    left: 420px;
    top: 275px;
    width: 574px;
    height: 5px;
    background: var(--accent-purple);
  }
  .contact {
    position: absolute;
    left: 425px;
    margin: 0;
    line-height: 1;
    white-space: nowrap;
  }
  .contact-name {
    top: 306px;
    font-size: 44px;
    font-weight: 700;
    font-style: italic;
  }
  .contact-line {
    font-size: 46px;
    font-weight: 400;
  }
  .contact-title { top: 376px; }
  .contact-mobile { top: 441px; }
  .contact-email { top: 507px; }
  .contact-web { top: 573px; }
</style>
</head>
<body>
  <main class="card">
    <h1 class="brand-name">Maple HR</h1>
    <div class="divider"></div>
    <p class="contact contact-name">Marta Oldenbrook</p>
    <p class="contact contact-line contact-title">Managing Director</p>
    <p class="contact contact-line contact-mobile">m: 0438 615 209</p>
    <p class="contact contact-line contact-email">e:&nbsp; marta@maplehr.com.au</p>
    <p class="contact contact-line contact-web">www.maplehr.com.au</p>
  </main>
</body>
</html>
```